Change of Address Card

We are fertility physicians in New York . Need a change of address postcard .

The front should be colorful
contain the statement " we are moving!"
and the names Lorenzo Bettuni MD, Oksana Dremova MD

Also the front should contain the drawing of a sperm with either wings or wheeels or whatever your creativity suggests as long as it is not vulgar ( we are doctors !)

The back should contain
the address area and stamp area
and a text area
and possibly a recall of the drawing in front.
use same font

text below

Dear Friends and Colleagues

Lorenzo and Oksana are relocating their fertility practice to a new location on 418 West 71st Street, Suite 604, New York NY 10023
Please take note of our new phone number
Our New phone Number is 212-555-0194

Thank you for your support!

Target Market(s)

this is a card that goes to physicians

Industry/Entity Type

It Support

Requirements
Must have
• fit standard postcard size
Rectangular
At least 3-1/2 inches high x 5 inches long x 0.007 inch thick
No more than 4-1/4 inches high x 6 inches long x 0.016 inches thick
will not be mailed in an envelope

```html
<!DOCTYPE html>
<html lang="en">
<head>
<meta charset="utf-8">
<title>Change of Address Postcard – Back</title>
<link rel="stylesheet" href="https://fonts.googleapis.com/css2?family=Libre+Baskerville:wght@700&display=swap">
<style>
  :root {
    --sheet: #ffffff;
    --card: #f6f07c;
    --ink: #111111;
    --accent: #e3232b;
    --mascot-light: #fbd6ca;
    --mascot: #f4b6a6;
    --rule: #6e6a3a;
    --crop: #9a9a9a;
  }
  html, body {
    margin: 0;
    padding: 0;
    width: 1200px;
    height: 858px;
    overflow: hidden;
    background: var(--sheet);
  }
  .sheet {
    position: relative;
    width: 1200px;
    height: 858px;
    background: var(--sheet);
  }
  .crop-marks {
    position: absolute;
    inset: 0;
  }
  .postcard {
    position: absolute;
    left: 67px;
    top: 53px;
    width: 1067px;
    height: 739px;
    background: var(--card);
  }
  .mascot-placeholder {
    position: absolute;
    left: 200px;
    top: 40px;
    width: 386px;
    height: 186px;
    border-radius: 24px;
    background: radial-gradient(ellipse at 40% 40%, var(--mascot-light), var(--mascot));
  }
  .message {
    position: absolute;
    left: 47px;
    top: 0;
    font-family: "Libre Baskerville", Georgia, serif;
    font-weight: 700;
    font-size: 24px;
    letter-spacing: 1px;
    color: var(--ink);
  }
  .message .line {
    position: absolute;
    left: 0;
    margin: 0;
    white-space: nowrap;
    line-height: 1;
  }
  .message .accent { color: var(--accent); }
  .stamp-box {
    position: absolute;
    left: 860px;
    top: 71px;
    width: 126px;
    height: 122px;
    border: 2px dashed var(--ink);
    box-sizing: border-box;
  }
  .address-lines {
    position: absolute;
    left: 658px;
    top: 0;
    width: 360px;
  }
  .address-lines .rule {
    position: absolute;
    left: 0;
    width: 360px;
    border-top: 1.5px dashed var(--rule);
  }
</style>
</head>
<body>
<div class="sheet">
  <svg class="crop-marks" width="1200" height="858" viewBox="0 0 1200 858" aria-hidden="true">
    <g stroke="var(--crop)" stroke-width="1.5">
      <line x1="95" y1="0" x2="95" y2="34"/>
      <line x1="0" y1="86" x2="40" y2="86"/>
      <line x1="1105" y1="0" x2="1105" y2="34"/>
      <line x1="1160" y1="86" x2="1200" y2="86"/>
      <line x1="95" y1="824" x2="95" y2="858"/>
      <line x1="0" y1="770" x2="40" y2="770"/>
      <line x1="1105" y1="824" x2="1105" y2="858"/>
      <line x1="1160" y1="770" x2="1200" y2="770"/>
    </g>
  </svg>

  <section class="postcard">
    <div class="mascot-placeholder" role="img" aria-label="Friendly winged mascot illustration recalling the front of the card"></div>

    <div class="message">
      <p class="line" style="top:230px">Dear Friends and Colleagues</p>
      <p class="line" style="top:287px">Lorenzo and Oksana are relocating</p>
      <p class="line" style="top:318px">their fertility practice</p>
      <p class="line" style="top:353px">to a new location on</p>
      <p class="line accent" style="top:389px">418 West 71st Street, Suite 604,</p>
      <p class="line accent" style="top:424px">New York NY 10023</p>
      <p class="line" style="top:489px">Please take note of our new phone number</p>
      <p class="line" style="top:520px">Our New phone Number is <span class="accent">212-555-0194</span></p>
      <p class="line" style="top:584px">Thank you for your support!</p>
    </div>

    <div class="stamp-box" aria-label="Stamp area"></div>

    <div class="address-lines" aria-label="Address area">
      <div class="rule" style="top:387px"></div>
      <div class="rule" style="top:432px"></div>
      <div class="rule" style="top:477px"></div>
      <div class="rule" style="top:522px"></div>
      <div class="rule" style="top:572px"></div>
      <div class="rule" style="top:622px"></div>
      <div class="rule" style="top:669px"></div>
    </div>
  </section>
</div>
</body>
</html>
```